Beauty Studio Business Card Design

its a new business & I want something different and classy
the strips are part of my decor

Target Market(s)

young girls and mature women

Industry/Entity Type

Business

Contact Information for Business Card

Frae-la-mu 26 0459817362 ABN # all on the front
address on the back + apt times & maybe my name
I would like black & white strips & fancy font with a fancy border around Frae-la-mu

```html
<!DOCTYPE html>
<html lang="en">
<head>
<meta charset="utf-8">
<title>Frae-la-mu Business Card</title>
<link rel="stylesheet" href="https://fonts.googleapis.com/css2?family=Open+Sans:wght@400;700&display=swap">
<style>
  :root {
    --backdrop: #e6e6e6;
    --ink: #111111;
    --white: #f2f2f2;
    --paper: #f7f7f7;
    --black: #050505;
    --wine: #4a0a0e;
    --red: #c8242b;
    --grey-panel: #a2a3a5;
    --edge-grey: #8d8d8d;
    --line: #333333;
  }
  * { box-sizing: border-box; margin: 0; padding: 0; }
  html, body { width: 1200px; height: 1200px; overflow: hidden; }
  body {
    background: var(--backdrop);
    font-family: "Open Sans", Arial, sans-serif;
    position: relative;
  }
  .card {
    position: absolute;
    left: 250px;
    width: 700px;
    height: 400px;
    overflow: hidden;
    box-shadow: 0 6px 18px rgba(0,0,0,0.18);
  }
  .card--front { top: 150px; }
  .card--back { top: 650px; background: var(--paper); }

  .front-waves { position: absolute; inset: 0; width: 100%; height: 100%; }

  .brand {
    position: absolute;
    display: flex;
    align-items: center;
    gap: 12px;
    font-weight: 700;
    color: var(--ink);
    letter-spacing: 0.5px;
  }
  .brand__dot {
    width: 18px; height: 18px; border-radius: 50%;
    background: var(--red);
  }
  .card--front .brand { left: 200px; top: 178px; font-size: 38px; }

  .abn {
    position: absolute;
    left: 330px;
    top: 300px;
    color: #ffffff;
    font-size: 17px;
    line-height: 1.35;
    text-align: left;
  }

  .back-panel {
    position: absolute;
    left: 0; top: 0; bottom: 0;
    width: 330px;
    background: var(--grey-panel);
    border-right: 3px solid var(--ink);
  }
  .card--back .brand { left: 50px; top: 172px; font-size: 36px; }

  .contact {
    position: absolute;
    right: 38px;
    top: 30px;
    text-align: right;
    font-size: 19px;
    line-height: 1.3;
    color: var(--ink);
  }
  .appointments {
    position: absolute;
    left: 366px;
    top: 150px;
    width: 300px;
  }
  .appointments__label { font-size: 19px; color: var(--ink); margin-bottom: 6px; }
  .appointments__line {
    height: 36px;
    border-bottom: 1.5px solid var(--line);
  }
</style>
</head>
<body>

<section class="card card--front" aria-label="Business card front">
  <svg class="front-waves" viewBox="0 0 700 400" preserveAspectRatio="none" aria-hidden="true">
    <defs>
      <linearGradient id="wine-top" x1="0" y1="0" x2="1" y2="1">
        <stop offset="0" stop-color="#000000"/>
        <stop offset="0.55" stop-color="#1a0204"/>
        <stop offset="1" stop-color="#5a0c12"/>
      </linearGradient>
      <linearGradient id="wine-bottom" x1="0" y1="1" x2="1" y2="0">
        <stop offset="0" stop-color="#4a0a0e"/>
        <stop offset="0.5" stop-color="#1a0204"/>
        <stop offset="1" stop-color="#000000"/>
      </linearGradient>
    </defs>
    <rect width="700" height="400" fill="url(#wine-top)"/>
    <path d="M0,250 C220,330 430,150 700,250 L700,400 L0,400 Z" fill="url(#wine-bottom)"/>
    <path d="M0,110 C230,40 430,240 700,140 L700,262 C430,165 230,345 0,262 Z" fill="#8d8d8d"/>
    <path d="M0,110 C230,40 430,240 700,140 L700,250 C430,152 230,332 0,250 Z" fill="#f0f0f0"/>
    <path d="M0,400 L0,330 C240,360 420,230 700,300 L700,400 Z" fill="#050505"/>
  </svg>

  <div class="brand">
    <span class="brand__dot"></span>
    <span class="brand__name">Frae-la-mu</span>
  </div>

  <p class="abn">ABN<br>26 0459817362</p>
</section>

<section class="card card--back" aria-label="Business card back">
  <div class="back-panel"></div>

  <div class="brand">
    <span class="brand__dot"></span>
    <span class="brand__name">Frae-la-mu</span>
  </div>

  <div class="contact">
    <p>Name</p>
    <p>555-555-555</p>
    <p>email@email.com</p>
  </div>

  <div class="appointments">
    <p class="appointments__label">Appointment Times:</p>
    <div class="appointments__line"></div>
    <div class="appointments__line"></div>
    <div class="appointments__line"></div>
    <div class="appointments__line"></div>
    <div class="appointments__line"></div>
  </div>
</section>

</body>
</html>
```